Stationary and Business card design for a residential window and door manufacturing company
residential window and door manufacturing company
Simple
Tom Ashdale
General Manager
3870 Pellham Ridge Rd Toronto, ON M8K 2T6
t.ashdale@solvarowindowsanddoors.com
solvarowindowsanddoors.com
Side ways logo

```html
<!DOCTYPE html>
<html lang="en">
<head>
<meta charset="utf-8">
<title>Solvaro Windows &amp; Doors – Business Card</title>
<link href="https://fonts.googleapis.com/css2?family=Open+Sans:wght@400;600;700&display=swap" rel="stylesheet">
<style>
  :root {
    --ink: #0d0d0d;
    --paper: #ffffff;
    --brand-red: #d3212b;
    --muted: #9a9a9a;
    --light-text: #e9e9e9;
    --stage: #e4e4e2;
  }
  * { box-sizing: border-box; margin: 0; padding: 0; }
  html, body { width: 1200px; height: 904px; overflow: hidden; }
  body {
    background: var(--stage);
    font-family: "Open Sans", Arial, sans-serif;
    position: relative;
  }
  .card {
    position: absolute;
    width: 600px;
    height: 343px;
    border-radius: 4px;
    overflow: hidden;
    box-shadow: 0 10px 28px rgba(0,0,0,.22);
  }
  .card--front {
    left: 170px; top: 110px;
    background: var(--ink);
    display: flex; align-items: center; justify-content: center;
  }
  .brand {
    display: flex; align-items: center; gap: 12px;
    color: var(--paper);
    font-weight: 700;
    font-size: 34px;
    letter-spacing: 1px;
  }
  .brand__mark {
    width: 18px; height: 18px;
    background: var(--brand-red);
  }
  .card--back {
    left: 430px; top: 420px;
    background: var(--paper);
  }
  .back__top {
    position: absolute; left: 0; top: 0; width: 100%; height: 150px;
    padding: 48px 0 0 42px;
  }
  .back__top .brand { color: var(--ink); font-size: 30px; }
  .holder { margin-top: 22px; }
  .holder__name { color: var(--brand-red); font-weight: 700; font-size: 17px; line-height: 1.2; }
  .holder__title { color: var(--ink); font-size: 12px; }
  .back__band {
    position: absolute; left: 0; top: 180px; width: 100%; height: 163px;
    background: var(--ink);
    padding: 16px 0 0 42px;
    color: var(--light-text);
    font-size: 12px;
  }
  .address { line-height: 1.45; margin-bottom: 8px; }
  .contact-list { list-style: none; }
  .contact-list li { display: flex; align-items: center; gap: 9px; line-height: 1.6; }
  .contact-list svg { width: 11px; height: 11px; fill: var(--brand-red); flex: none; }
</style>
</head>
<body>
  <section class="card card--front" aria-label="Card front">
    <div class="brand"><span class="brand__mark"></span>Solvaro</div>
  </section>

  <section class="card card--back" aria-label="Card back">
    <div class="back__top">
      <div class="brand"><span class="brand__mark"></span>Solvaro</div>
      <div class="holder">
        <p class="holder__name">Tom Ashdale</p>
        <p class="holder__title">General Manager</p>
      </div>
    </div>
    <div class="back__band">
      <p class="address">3870 Pellham Ridge Rd<br>Toronto, ON M8K 2T6</p>
      <ul class="contact-list">
        <li><svg viewBox="0 0 24 24" aria-hidden="true"><path d="M6.6 10.8a15.1 15.1 0 0 0 6.6 6.6l2.2-2.2a1 1 0 0 1 1-.25 11.4 11.4 0 0 0 3.6.57 1 1 0 0 1 1 1V20a1 1 0 0 1-1 1A17 17 0 0 1 3 4a1 1 0 0 1 1-1h3.5a1 1 0 0 1 1 1c0 1.25.2 2.45.57 3.57a1 1 0 0 1-.25 1z"/></svg>905.555.0148</li>
        <li><svg viewBox="0 0 24 24" aria-hidden="true"><path d="M7 1h10a2 2 0 0 1 2 2v18a2 2 0 0 1-2 2H7a2 2 0 0 1-2-2V3a2 2 0 0 1 2-2zm0 3v14h10V4zm5 15.5a1.2 1.2 0 1 0 0 2.4 1.2 1.2 0 0 0 0-2.4z"/></svg>416.555.0193</li>
        <li><svg viewBox="0 0 24 24" aria-hidden="true"><path d="M2 5h20v14H2zm2 2v.5l8 5 8-5V7zm0 2.8V17h16V9.8l-8 5z"/></svg>t.ashdale@solvarowindowsanddoors.com</li>
        <li><svg viewBox="0 0 24 24" aria-hidden="true"><path d="M12 2a10 10 0 1 0 0 20 10 10 0 0 0 0-20zm6.9 6h-3a15.7 15.7 0 0 0-1.3-3.6A8 8 0 0 1 18.9 8zM12 4c.8 1.2 1.5 2.5 1.9 4h-3.8c.4-1.5 1.1-2.8 1.9-4zM4.3 14a8 8 0 0 1 0-4h3.4a16 16 0 0 0 0 4zm.8 2h3a15.7 15.7 0 0 0 1.3 3.6A8 8 0 0 1 5.1 16zm3-8h-3a8 8 0 0 1 4.3-3.6A15.7 15.7 0 0 0 8.1 8zM12 20c-.8-1.2-1.5-2.5-1.9-4h3.8c-.4 1.5-1.1 2.8-1.9 4zm2.3-6H9.7a14 14 0 0 1 0-4h4.6a14 14 0 0 1 0 4zm.3 5.6a15.7 15.7 0 0 0 1.3-3.6h3a8 8 0 0 1-4.3 3.6zm1.7-5.6a16 16 0 0 0 0-4h3.4a8 8 0 0 1 0 4z"/></svg>solvarowindowsanddoors.com</li>
      </ul>
    </div>
  </section>
</body>
</html>
```